Breezeway Climate Business Card Design

Design new, 2 sides, business cards for a residential and light commercial heating, air conditioning contractor.

Target Market(s)

Homeowners, small businesses

Industry/Entity Type

Business

Contact Information for Business Card

Dominic Vasquerelli
Phone - 555-214-6837
Email
Address - PO box 618
Millbrook NJ 07999
Website - www.BreezewayClimateLLC.example

Requirements
Must have
• logo, company colors, standard size with no die cut, so I can use printhaven

```html
<!DOCTYPE html>
<html lang="en">
<head>
<meta charset="utf-8">
<title>Breezeway Climate Business Card</title>
<link rel="stylesheet" href="https://fonts.googleapis.com/css2?family=Lato:wght@400;700;900&family=Arimo:wght@400&display=swap">
<style>
  :root {
    --bg: #e4e4e4;
    --card: #ffffff;
    --brand-red: #9b1b30;
    --ink: #2b2b2b;
    --rule: #1e1e1e;
    --shadow: rgba(0, 0, 0, 0.18);
  }
  * { box-sizing: border-box; margin: 0; padding: 0; }
  html, body {
    width: 1200px;
    height: 997px;
    overflow: hidden;
    background: var(--bg);
  }
  .sheet {
    position: relative;
    width: 1200px;
    height: 997px;
  }
  .card {
    position: absolute;
    left: 250px;
    width: 700px;
    height: 400px;
    background: var(--card);
    box-shadow: 0 6px 24px var(--shadow);
  }
  .card--front { top: 68px; }
  .card--back { top: 528px; }

  /* Front */
  .front-brand {
    position: absolute;
    inset: 0;
    display: flex;
    align-items: center;
    justify-content: center;
    gap: 18px;
  }
  .brand-dot {
    width: 30px;
    height: 30px;
    border-radius: 50%;
    background: var(--brand-red);
  }
  .brand-name {
    font-family: "Lato", sans-serif;
    font-weight: 900;
    color: var(--brand-red);
    letter-spacing: 0.02em;
  }
  .front-brand .brand-name { font-size: 50px; }

  /* Back */
  .back-brand {
    position: absolute;
    top: 48px;
    right: 44px;
    display: flex;
    align-items: center;
    gap: 10px;
  }
  .back-brand .brand-dot { width: 16px; height: 16px; }
  .back-brand .brand-name { font-size: 26px; }

  .holder {
    position: absolute;
    left: 40px;
    top: 168px;
    right: 44px;
  }
  .holder-row {
    display: flex;
    align-items: flex-end;
    gap: 10px;
  }
  .holder-name {
    font-family: "Lato", sans-serif;
    font-weight: 900;
    font-size: 25px;
    color: var(--brand-red);
    line-height: 1;
    white-space: nowrap;
  }
  .holder-rule {
    flex: 1;
    height: 2px;
    background: var(--rule);
    margin-bottom: 2px;
  }
  .holder-title {
    margin-top: 5px;
    font-family: "Lato", sans-serif;
    font-weight: 700;
    font-size: 13px;
    letter-spacing: 0.03em;
    color: var(--ink);
  }

  .contact-list {
    position: absolute;
    left: 40px;
    top: 246px;
    list-style: none;
    font-family: "Arimo", sans-serif;
    font-size: 16px;
    color: var(--ink);
  }
  .contact-item {
    display: flex;
    align-items: flex-start;
    gap: 16px;
    margin-bottom: 12px;
    line-height: 1.35;
  }
  .contact-icon {
    flex: none;
    width: 20px;
    height: 20px;
    margin-top: 1px;
  }

  .website {
    position: absolute;
    right: 44px;
    bottom: 92px;
    font-family: "Lato", sans-serif;
    font-weight: 700;
    font-size: 16px;
    letter-spacing: 0.14em;
    color: var(--brand-red);
  }
</style>
</head>
<body>
<main class="sheet">

  <section class="card card--front" aria-label="Business card front">
    <div class="front-brand">
      <span class="brand-dot"></span>
      <span class="brand-name">Breezeway Climate</span>
    </div>
  </section>

  <section class="card card--back" aria-label="Business card back">
    <div class="back-brand">
      <span class="brand-dot"></span>
      <span class="brand-name">Breezeway Climate</span>
    </div>

    <div class="holder">
      <div class="holder-row">
        <span class="holder-name">Marisol Drayton</span>
        <span class="holder-rule"></span>
      </div>
      <div class="holder-title">FOUNDER &amp; CEO</div>
    </div>

    <ul class="contact-list">
      <li class="contact-item">
        <svg class="contact-icon" viewBox="0 0 20 20" aria-hidden="true">
          <circle cx="10" cy="10" r="10" fill="#9b1b30"/>
          <path d="M6.3 5.5l2 -.3 1 2.3 -1.2 1a6 6 0 0 0 3.3 3.3l1-1.2 2.3 1-.3 2c-4.6.3-8.4-3.5-8.1-8.1z" fill="#fff"/>
        </svg>
        <span>+1 (555) 302-4418</span>
      </li>
      <li class="contact-item">
        <svg class="contact-icon" viewBox="0 0 20 20" aria-hidden="true">
          <circle cx="10" cy="10" r="10" fill="#9b1b30"/>
          <path d="M10 4.8l5 4.4h-1.5v5h-2.6v-3h-1.8v3H6.5v-5H5z" fill="#fff"/>
        </svg>
        <span>md@bc.example</span>
      </li>
      <li class="contact-item">
        <svg class="contact-icon" viewBox="0 0 20 20" aria-hidden="true">
          <circle cx="10" cy="10" r="10" fill="#9b1b30"/>
          <path d="M10 4.5a3.6 3.6 0 0 0-3.6 3.6c0 2.7 3.6 7.2 3.6 7.2s3.6-4.5 3.6-7.2A3.6 3.6 0 0 0 10 4.5z" fill="#fff"/>
          <circle cx="10" cy="8.1" r="1.4" fill="#9b1b30"/>
        </svg>
        <span>42 Linden Court, 1st Floor,<br>Millbrook, NJ 07999</span>
      </li>
    </ul>

    <div class="website">www.bc.example</div>
  </section>

</main>
</body>
</html>
```